Business Card Project for 'Manufacturing and Healthcare Business Improvement company.

I need a business card for a consulting company that does process improvement for manufacturing and healthcare companies. I had a contest for a logo, and I liked what we came up with for the logo.

I wasn't blown away by what I got for the business card. The designer tried and it was a decent design, but I was looking for a little more. I want something that looks professional, but is eye-catching enough that people say "that looks cool, where did you get it?"

I've uploaded some business card examples I found that I liked. Even though some of the examples have red and orange on them, I think I would stick with blues, grays and blacks since that matches the logo theme. As awesome as some of them look, I don't think that a single color card, like an all-black card, will work for me; but feel free to change my mind.

It might also be possible to incorporate elements from the logo into the card. I also like some of the elements that use circles or rectangles etc to separate the phone number, website etc.

I like it when people have used geometric shapes to break up the card into sections or to add borders to the card to complement the logo, not compete with it for attention. For example, the red and gray example that has a curve that separates the card into two parts. I've wondered, how it would look if the red area were blue and had an arrow separating the top and bottom, like the arrow on the logo. Maybe on the back there could be an element that mirrors the bar graph and arrow. Would those look interesting, or would they compete with the other elements too much?

I also uploaded some examples of cards I made up, either based on ideas I saw elsewhere or based on design elements that the logo had in his designs. If you wonder why the ones with "lorem ipsum" look like an amateur did them, it's because they did.

I also think that I may add a QR code at some point, so I would need a location for that, along with something that says what the QR links to, such as, "scan here to upload contact information" or something similar. I don't know if I want cards that require having special designs cut, but if you have the idea, go with it.

I don't want to limit anyone's creativity, so I'll leave it at that.

Target Market(s)

Healthcare and Manufacturing

Industry/Entity Type

Manufacturing

Contact Information for Business Card

Harborline Advisory Group LLC.
Owen Prescott MBA, LSSMBB
Managing Partner
o.prescott@harborlineadvisorygroupllc.com
(555) 987-2310

Font styles to use
Serif
Sans Serif

Colors

Designer to choose only greyscale colors for use in the design.

Requirements
Must have
• The logo.
Nice to have
• Even though some of the examples I uploaded have red and orange on them, I think I would stick with blues, grays and blacks since that matches the logo theme.

I also like some of the elements that use circles or rectangles etc to separate the phone number, website etc.

I like it when people have used geometric shapes to break up the card into sections or to add borders to the card to complement the logo, not compete with it for attention.

For example, the red and gray example that has a curve that separates the card into two parts. I've wondered, how it would look if the red area were blue and had an arrow separating the top and bottom, like the arrow on the logo. Maybe on the back there could be an element that mirrors the bar graph and arrow. Would those look interesting, or would they compete with the other elements too much?

It might also be possible to incorporate elements from the logo into the card.

I also think that I may add a QR code at some point, so I would need a location for that, along with something that says what the QR links to, such as, "scan here to upload contact information" or something similar.

It could have something somewhere saying "We use Lean, Six Sigma and TPM continuous improvement tools to improve manufacturing and healthcare businesses."
Should not have
• So many colors and elements that it is distracting. Should not be generic.

As awesome as some of them look, I don't think that a single color card, like an all-black card, will work for me; but feel free to change my mind.

I don't know if I want cards that require having special designs cut, but if you have the idea, go with it.

```html
<!DOCTYPE html>
<html lang="en">
<head>
<meta charset="utf-8">
<title>Harborline Advisory Group LLC. – Business Card</title>
<link rel="stylesheet" href="https://fonts.googleapis.com/css2?family=Montserrat:wght@600&family=Roboto+Condensed:wght@400;500&display=swap">
<style>
  :root {
    --stage: #000000;
    --paper: #ffffff;
    --navy: #1f3a6d;
    --blue-deep: #244a85;
    --blue-bright: #2160b0;
    --icon-bg: #2b4b86;
    --grey-dark: #5f5f5f;
    --grey-light: #cfcfcf;
    --ink: #2a2a2a;
  }
  html, body {
    margin: 0;
    width: 1200px;
    height: 1200px;
    overflow: hidden;
    background: var(--stage);
  }
  .sheet { display: block; width: 1200px; height: 1200px; }
  .brand-name { font-family: "Montserrat", sans-serif; font-weight: 600; }
  .contact { font-family: "Roboto Condensed", sans-serif; font-weight: 500; fill: var(--ink); }
  .icon-disc { fill: var(--icon-bg); }
  .icon-glyph { fill: none; stroke: var(--paper); stroke-width: 2.6; stroke-linecap: round; stroke-linejoin: round; }
  .icon-solid { fill: var(--paper); }
  .divider-line { fill: none; stroke-linecap: round; }
</style>
</head>
<body>
<svg class="sheet" viewBox="0 0 1654 1654" xmlns="http://www.w3.org/2000/svg">
  <defs>
    <clipPath id="front-shape"><rect x="450" y="351" width="754" height="421" rx="55"/></clipPath>
    <clipPath id="back-shape"><rect x="450" y="881" width="754" height="421" rx="55"/></clipPath>
    <linearGradient id="blue-band" x1="0" y1="0" x2="1" y2="0">
      <stop offset="0" stop-color="var(--blue-deep)"/>
      <stop offset="1" stop-color="var(--blue-bright)"/>
    </linearGradient>
    <linearGradient id="blue-panel" x1="0" y1="1" x2="1" y2="0">
      <stop offset="0" stop-color="var(--blue-deep)"/>
      <stop offset="1" stop-color="var(--blue-bright)"/>
    </linearGradient>
    <linearGradient id="grey-line" x1="0" y1="0" x2="1" y2="0">
      <stop offset="0" stop-color="var(--grey-dark)"/>
      <stop offset="1" stop-color="var(--grey-light)"/>
    </linearGradient>
    <linearGradient id="grey-line-back" x1="0" y1="1" x2="1" y2="0">
      <stop offset="0" stop-color="var(--grey-dark)"/>
      <stop offset="1" stop-color="var(--grey-light)"/>
    </linearGradient>
  </defs>

  <!-- Front side -->
  <g class="card card-front" clip-path="url(#front-shape)">
    <rect x="450" y="351" width="754" height="421" fill="var(--paper)"/>
    <path class="divider-line" d="M450,620 Q820,690 1204,600" stroke="url(#grey-line)" stroke-width="10"/>
    <path class="band-blue" d="M450,660 Q820,720 1204,630 L1204,772 L450,772 Z" fill="url(#blue-band)"/>

    <g class="brand-lockup">
      <rect x="602" y="467" width="22" height="22" fill="var(--navy)"/>
      <text class="brand-name" x="640" y="493" font-size="58" fill="var(--navy)" letter-spacing="1">HARBORLINE</text>
      <text class="brand-name" x="827" y="548" font-size="29" fill="var(--navy)" text-anchor="middle" letter-spacing="1">ADVISORY GROUP LLC.</text>
    </g>
  </g>

  <!-- Back side -->
  <g class="card card-back" clip-path="url(#back-shape)">
    <rect x="450" y="881" width="754" height="421" fill="var(--paper)"/>
    <path class="divider-line" d="M870,881 Q920,1100 740,1302" stroke="url(#grey-line-back)" stroke-width="10"/>
    <path class="panel-blue" d="M890,881 Q940,1100 770,1302 L1204,1302 L1204,881 Z" fill="url(#blue-panel)"/>

    <g class="brand-lockup">
      <text class="brand-name" x="1045" y="1112" font-size="38" fill="var(--paper)" text-anchor="middle" letter-spacing="1">HARBORLINE</text>
      <text class="brand-name" x="1045" y="1142" font-size="18" fill="var(--paper)" text-anchor="middle" letter-spacing="1">ADVISORY GROUP LLC.</text>
    </g>

    <g class="contact-list">
      <text class="contact" x="802" y="993" font-size="16" text-anchor="end">(555) 987-2310</text>
      <text class="contact" x="802" y="1014" font-size="16" text-anchor="end">(555) 987-2310</text>
      <circle class="icon-disc" cx="837" cy="999" r="23"/>
      <path class="icon-solid" d="M827,988 c2,-2 5,-2 6,0 l3,5 c1,2 0,3 -1,4 l-2,2 c1,3 4,6 7,7 l2,-2 c1,-1 3,-2 4,-1 l5,3 c2,1 2,4 0,6 l-2,2 c-3,3 -9,1 -15,-5 c-6,-6 -8,-12 -5,-15 z"/>

      <text class="contact" x="797" y="1066" font-size="15" text-anchor="end">o.prescott@harborlineadvisorygroupllc.com</text>
      <circle class="icon-disc" cx="832" cy="1061" r="23"/>
      <rect class="icon-glyph" x="819" y="1052" width="26" height="18" rx="2"/>
      <path class="icon-glyph" d="M819,1053 L832,1063 L845,1053 M819,1069 L828,1060 M845,1069 L836,1060"/>

      <text class="contact" x="777" y="1120" font-size="20" text-anchor="end">www.harborlineadvisory.com</text>
      <circle class="icon-disc" cx="817" cy="1117" r="23"/>
      <circle class="icon-glyph" cx="817" cy="1117" r="14"/>
      <ellipse class="icon-glyph" cx="817" cy="1117" rx="6" ry="14"/>
      <path class="icon-glyph" d="M803,1117 H831 M805,1110 H829 M805,1124 H829"/>

      <text class="contact" x="574" y="1163" font-size="20">First Address line</text>
      <text class="contact" x="574" y="1184" font-size="20">Second Address line</text>
      <circle class="icon-disc" cx="783" cy="1169" r="23"/>
      <path class="icon-solid" d="M783,1155 L798,1168 L794,1168 L794,1182 L787,1182 L787,1174 L779,1174 L779,1182 L772,1182 L772,1168 L768,1168 Z"/>
    </g>
  </g>
</svg>
</body>
</html>
```